Employee I.D. Card - Badge

We need an employee I.D. card designed. Our employees are going to be wearing these. I would like to have it look nice. Something professional yet cool (not uptight if that makes sense).
Project Scope:
Vertical orientation
Company name ------------- (Bright and Tidy)
Website ------------- (brightandtidymn.example)
Employee Picture
background check image
front and back designed - same design on either side
You can create the card without having the employee images on them.
Here are the dimensions -
2.125 x 3.370 inches
Double sided - same design can be used front and back
Background badge - I would like to add an image that shows that the employee has taken a background check. I've added the press-kit for the company we use. If you have a better idea than incorporating their logo, we can certainly do something different.
Example image-
https://www.findwell-search.example/results?q=background+check+badge&mode=images
The print company will set up the names.
Logo is attached
Also attached are our business cards. You can use this for an idea of brand/company style.
Our website - brightandtidymn.example

```html
<!DOCTYPE html>
<html lang="en">
<head>
<meta charset="utf-8">
<title>Bright and Tidy – Employee ID Badge</title>
<link rel="stylesheet" href="https://fonts.googleapis.com/css2?family=Work+Sans:wght@400;500&display=swap">
<style>
  :root {
    --page-bg: #e0e1e1;
    --card-bg: #ffffff;
    --brand-blue: #0a78c2;
    --brand-sky: #00b0ec;
    --brand-green: #9ccb2e;
    --badge-gold: #d8b45a;
    --badge-dark: #2b2b2b;
    --photo-dark: #3b3c3b;
    --photo-warm: #c9a08a;
    --text-light: #ffffff;
  }
  * { box-sizing: border-box; margin: 0; padding: 0; }
  html, body {
    width: 1200px;
    height: 992px;
    overflow: hidden;
    background: var(--page-bg);
    font-family: "Work Sans", Arial, sans-serif;
  }
  .badge-sheet { position: relative; width: 1200px; height: 992px; }
  .id-card {
    position: absolute;
    top: 158px;
    width: 425px;
    height: 675px;
    background: var(--card-bg);
    overflow: hidden;
  }
  .id-card--front { left: 143px; }
  .id-card--back { left: 629px; }
  .card-swoosh { position: absolute; top: 0; left: 0; width: 425px; height: 675px; }
  .brand-name {
    position: absolute;
    top: 24px;
    left: 25px;
    width: 165px;
    font-weight: 500;
    font-size: 37px;
    line-height: 44px;
    color: var(--brand-blue);
    letter-spacing: -0.8px;
    white-space: nowrap;
  }
  .check-badge {
    position: absolute;
    top: 20px;
    left: 321px;
    width: 74px;
    height: 74px;
  }
  .employee-photo {
    position: absolute;
    left: 8px;
    top: 168px;
    width: 388px;
    height: 450px;
    border-radius: 120px 120px 0 0;
    background: linear-gradient(180deg, var(--photo-warm) 0%, var(--photo-dark) 55%, var(--photo-dark) 100%);
  }
  .web-band {
    position: absolute;
    left: 0;
    bottom: 0;
    width: 425px;
    height: 57px;
    background: linear-gradient(90deg, var(--brand-blue), var(--brand-sky));
    display: flex;
    align-items: center;
    justify-content: center;
  }
  .web-address {
    color: var(--text-light);
    font-size: 22px;
    font-weight: 400;
    letter-spacing: 0.4px;
  }
</style>
</head>
<body>
<main class="badge-sheet">
  <section class="id-card id-card--front">
    <svg class="card-swoosh" viewBox="0 0 425 675" aria-hidden="true">
      <defs>
        <linearGradient id="swooshBlueFront" x1="0" y1="0" x2="1" y2="0">
          <stop offset="0" stop-color="#00b0ec"/>
          <stop offset="1" stop-color="#0a78c2"/>
        </linearGradient>
      </defs>
      <path d="M192,0 C198,140 295,205 360,280 C395,320 418,370 425,410 L425,0 Z" fill="#9ccb2e"/>
      <path d="M203,0 C209,130 300,192 362,264 C397,304 418,342 425,362 L425,0 Z" fill="#ffffff"/>
      <path d="M208,0 C214,125 302,185 364,255 C398,293 418,330 425,345 L425,0 Z" fill="url(#swooshBlueFront)"/>
    </svg>
    <div class="brand-name">Bright<br>and Tidy</div>
    <svg class="check-badge" viewBox="0 0 74 74" aria-hidden="true">
      <circle cx="37" cy="37" r="34" fill="#2b2b2b" stroke="#d8b45a" stroke-width="5"/>
    </svg>
    <div class="employee-photo" role="img" aria-label="Employee portrait photo"></div>
    <div class="web-band"><span class="web-address">brightandtidymn.example</span></div>
  </section>

  <section class="id-card id-card--back">
    <svg class="card-swoosh" viewBox="0 0 425 675" aria-hidden="true">
      <defs>
        <linearGradient id="swooshBlueBack" x1="0" y1="0" x2="1" y2="0">
          <stop offset="0" stop-color="#00b0ec"/>
          <stop offset="1" stop-color="#0a78c2"/>
        </linearGradient>
      </defs>
      <path d="M192,0 C198,140 295,205 360,280 C395,320 418,370 425,410 L425,0 Z" fill="#9ccb2e"/>
      <path d="M203,0 C209,130 300,192 362,264 C397,304 418,342 425,362 L425,0 Z" fill="#ffffff"/>
      <path d="M208,0 C214,125 302,185 364,255 C398,293 418,330 425,345 L425,0 Z" fill="url(#swooshBlueBack)"/>
    </svg>
    <div class="brand-name">Bright<br>and Tidy</div>
    <svg class="check-badge" viewBox="0 0 74 74" aria-hidden="true">
      <circle cx="37" cy="37" r="34" fill="#2b2b2b" stroke="#d8b45a" stroke-width="5"/>
    </svg>
    <div class="employee-photo" role="img" aria-label="Employee portrait photo"></div>
    <div class="web-band"><span class="web-address">brightandtidymn.example</span></div>
  </section>
</main>
</body>
</html>
```